Business Card Design for a Private Label Pet Company

We need a business card design for our family-owned company, Hollow Creek Pet Works (www.hollowcreekpetworks.com), out of St. Louis, MO. We provide turnkey private label solutions for retailers, Marketvale sellers and other brands who want to provide high quality, natural, Made in the USA pet products to their customers. Our customer are worldwide and range from the US to the UK to Vietnam and beyond. We offer private label for dozens of pet products including grooming products (shampoos, conditioners, colognes, ear and eye washes, mouthwash, etc.), all meat treats, supplements, and specialty products (pet stain and odor cleaner, anti-chew spray, etc.). We would like to see designs that use the colors, fonts and logos (see variations) within our brand guidelines and fit with the look and feel from our website.

Target Market(s)

Pet Store Owners, Marketvale Sellers, Pet Brand Marketers

Industry/Entity Type

Pet

Contact Information for Business Card

Tom Willoughby
CEO
Hollow Creek Pet Works
5817 Brookhaven Commerce Lane
St. Louis, MO 63521
office: 314.555.0182
mobile: 770.555.0139
email: tom@hollowcreekpetworks.com

Colors

Designer to choose colors to be used in the design.

Requirements
Must have
• Need to follow the brand guidelines attached for colors, fonts and logos
• Need to use the logos attached (or a variation) with our without the tagline
• Name, title, phone (office and mobil), email, address on the business card
• Clean professional look and feel that says: high quality natural pet products, high quality service, made in the USA
Nice to have
• Made in the USA is a big positive in our industry and we are very proud of it. There is an attached icon from our website. The designer can get creative here as they wish.
• I do like using color for pop. Just don't like lots of bright, loud colors.
Should not have
• lots of bright, loud colors
• overwhelming to the reader
• crowded

```html
<!DOCTYPE html>
<html lang="en">
<head>
<meta charset="utf-8">
<title>Hollow Creek Pet Works – Business Card</title>
<link rel="stylesheet" href="https://fonts.googleapis.com/css2?family=Montserrat:wght@300;400;600;700&display=swap">
<style>
  :root {
    --bg: #2b2e31;
    --card: #f7f7f5;
    --green: #647b36;
    --slate: #3f5b5e;
    --grey: #8c8c88;
    --white: #ffffff;
  }
  html, body {
    margin: 0; padding: 0;
    width: 1200px; height: 1000px;
    overflow: hidden;
    background: var(--bg);
    font-family: "Montserrat", Arial, sans-serif;
  }
  .card {
    position: absolute;
    left: 250px;
    width: 700px; height: 400px;
    background: var(--card);
    overflow: hidden;
  }
  .card--front { top: 60px; }
  .card--back { top: 540px; }
  .card__wave { position: absolute; inset: 0; }

  .brand { position: absolute; display: flex; align-items: center; gap: 12px; }
  .brand__dot { width: 16px; height: 16px; border-radius: 50%; background: var(--green); flex: none; }
  .brand__name {
    font-weight: 700; color: var(--slate);
    font-size: 30px; letter-spacing: 0.5px; text-transform: uppercase; line-height: 1.05;
  }
  .card--front .brand { left: 90px; top: 128px; }
  .card--front .brand__name { font-size: 34px; }
  .brand__url {
    position: absolute; left: 118px; top: 222px;
    font-size: 15px; color: var(--grey); letter-spacing: 0.6px;
  }
  .card--back .brand { left: 395px; top: 140px; }
  .card--back .brand__name { font-size: 26px; }

  .contact__line {
    position: absolute; left: 60px; top: 94px; width: 0; height: 80px;
    border-left: 3px solid var(--green);
  }
  .contact__icon {
    position: absolute; left: 46px; width: 30px; height: 30px;
  }
  .contact__text {
    position: absolute; left: 90px; font-size: 13px; color: var(--grey); line-height: 1.45; white-space: nowrap;
  }
  .name { top: 34px; font-size: 20px; letter-spacing: 0.5px; text-transform: uppercase; font-weight: 300; line-height: 1.1; }
  .name b { color: var(--green); font-weight: 700; }
  .name small { display: block; font-size: 12px; font-weight: 400; }
  .strong { color: var(--green); font-weight: 600; }
  .badge {
    position: absolute; right: 40px; bottom: 28px;
    width: 82px; height: 82px; border: 3px solid var(--white); border-radius: 6px; box-sizing: border-box;
  }
</style>
</head>
<body>

<section class="card card--front" aria-label="Card front">
  <svg class="card__wave" viewBox="0 0 700 400" aria-hidden="true">
    <path d="M455 0 L700 0 L700 335 C640 320 595 250 565 165 C535 80 520 20 455 0 Z" fill="var(--green)"/>
  </svg>
  <div class="brand"><span class="brand__dot"></span><span class="brand__name">Hollow Creek<br>Pet Works</span></div>
  <div class="brand__url">www.hollowcreekpetworks.com</div>
</section>

<section class="card card--back" aria-label="Card back">
  <svg class="card__wave" viewBox="0 0 700 400" aria-hidden="true">
    <path d="M0 262 C90 248 150 318 260 352 C340 378 420 362 520 334 C600 310 650 268 700 255 L700 400 L0 400 Z" fill="var(--green)"/>
  </svg>

  <div class="contact__line"></div>

  <svg class="contact__icon" style="top:34px" viewBox="0 0 30 30" aria-hidden="true">
    <circle cx="15" cy="15" r="15" fill="var(--green)"/>
    <circle cx="15" cy="12" r="4.5" fill="var(--white)"/>
    <path d="M7 23 C8 17 22 17 23 23 Z" fill="var(--white)"/>
  </svg>
  <svg class="contact__icon" style="top:84px" viewBox="0 0 30 30" aria-hidden="true">
    <circle cx="15" cy="15" r="15" fill="var(--green)"/>
    <path d="M10 8 L13 8 L14 12 L12 13.5 C13 16 14 17 16.5 18 L18 16 L22 17 L22 20 C22 21 21 22 20 22 C14 21.5 8.5 16 8 10 C8 9 9 8 10 8 Z" fill="var(--white)"/>
  </svg>
  <svg class="contact__icon" style="top:124px" viewBox="0 0 30 30" aria-hidden="true">
    <circle cx="15" cy="15" r="15" fill="var(--green)"/>
    <g fill="none" stroke="var(--white)" stroke-width="1.6">
      <circle cx="15" cy="15" r="7"/>
      <ellipse cx="15" cy="15" rx="3" ry="7"/>
      <line x1="8" y1="15" x2="22" y2="15"/>
    </g>
  </svg>
  <svg class="contact__icon" style="top:164px" viewBox="0 0 30 30" aria-hidden="true">
    <circle cx="15" cy="15" r="15" fill="var(--green)"/>
    <path d="M15 7 C11.5 7 9.5 9.5 9.5 12.5 C9.5 16.5 15 23 15 23 C15 23 20.5 16.5 20.5 12.5 C20.5 9.5 18.5 7 15 7 Z" fill="var(--white)"/>
    <circle cx="15" cy="12.5" r="2.2" fill="var(--green)"/>
  </svg>

  <div class="contact__text name"><b>Tom</b> Willoughby<small>CEO</small></div>
  <div class="contact__text" style="top:88px">314.555.0182 (Office)<br>770.555.0139 (Mobile)</div>
  <div class="contact__text" style="top:128px">tom@<span class="strong">hollowcreekpetworks</span>.com<br>www.<span class="strong">hollowcreekpetworks</span>.com</div>
  <div class="contact__text" style="top:168px"><span class="strong">Hollow Creek Pet Works</span><br>5817 Brookhaven Commerce Lane<br>St. Louis, MO 63521</div>

  <div class="brand"><span class="brand__dot"></span><span class="brand__name">Hollow Creek<br>Pet Works</span></div>

  <div class="badge" role="img" aria-label="Made in the USA badge"></div>
</section>

</body>
</html>
```